Billboard design for a small town Oral Surgeon

We are getting several billboards and need a design that highlights the doctors photo, and bullet points of what he does. Our business name is extremely long, so it’s a challenge to figure out how to do this. Maybe just use our logo? Open to ideas.
The logo can be shortened as designer sees fit, meaning we can drop the tag line. Important info to include:
Doctors name is Lorvik Tamsen
The highlighted bullet points are:
•Implants
•wisdom teeth
•Jaw Surgery
•facial trauma
The goal of this billboard is to let our community know that they have an option here in Ada, our town. Many still drive to the city a couple hours away not knowing they now have an option here at home. Having a hard time finding examples of what I have in mind, so hoping this will get us going. I want it as “non-busy” as possible, so no unnecessary lines or anything that competes with the information we are trying to get across.

Target Market(s)

Everyone in town, just trying to spread the word that we are here

Industry/Entity Type

Medical/surgical (oral surgery)

Font styles to use
Sans Serif

Colors
0094D4
00A9DD
6FCCEA
C7EBF8
E9F6FB

Requirements
Must have
• *New note** Due to location of billboard, I prefer the photo of doctor to be on the left side. Must look neat and professional. Must highlight what we do.
Nice to have
• Our colors are a blue-green with silver, against black or white, but I’m flexible on this, I don’t necessarily need the colors highlighted. I’m also flexible on font style, just needs to be easy to read.
Should not have
• Distracting graphics, should not look like a dental office. That’s an issue we have is people thinking we are another dental office, we do not do any general dentistry, it’s surgery only.

```html
<!DOCTYPE html>
<html lang="en">
<head>
<meta charset="utf-8">
<title>Kestrel Oral Surgery Billboard</title>
<link href="https://fonts.googleapis.com/css2?family=Montserrat:wght@700;800&display=swap" rel="stylesheet">
<style>
  :root {
    --teal: #168ea8;
    --silver: #9b9b9d;
    --ink: #0b0b0b;
    --white: #ffffff;
    --alert: #e4252b;
    --backdrop: #c4c4c4;
  }
  html, body {
    margin: 0;
    width: 1200px;
    height: 1058px;
    overflow: hidden;
    background: var(--backdrop);
    font-family: "Montserrat", Arial, sans-serif;
  }
  .billboard {
    position: absolute;
    left: 20px;
    top: 335px;
    width: 1160px;
    height: 388px;
    background: var(--white);
    overflow: hidden;
  }
  .billboard-shapes {
    position: absolute;
    inset: 0;
  }
  .doctor-photo {
    position: absolute;
    left: 0;
    top: 20px;
    width: 292px;
    height: 300px;
    clip-path: polygon(0 0, 188px 0, 188px 110px, 292px 210px, 292px 300px, 0 300px);
    background: linear-gradient(180deg, #c9a08a 0%, #b88a74 45%, #1c2130 70%, #141826 100%);
  }
  .doctor-name {
    position: absolute;
    left: 198px;
    top: 32px;
    color: var(--white);
    font-weight: 800;
    font-size: 25px;
    line-height: 1;
  }
  .practice-name {
    position: absolute;
    left: 395px;
    top: 92px;
    width: 230px;
    text-align: center;
    color: var(--teal);
    font-weight: 800;
    font-size: 36px;
    line-height: 1.15;
  }
  .services {
    position: absolute;
    left: 618px;
    top: 40px;
    margin: 0;
    padding: 0;
    list-style: none;
  }
  .service {
    display: flex;
    align-items: center;
    height: 61px;
    color: var(--ink);
    font-weight: 800;
    font-size: 48px;
    letter-spacing: 0.5px;
  }
  .service svg {
    width: 50px;
    height: 50px;
    margin-right: 20px;
    flex: none;
  }
  .location-tab {
    position: absolute;
    left: 958px;
    top: 286px;
    color: var(--white);
    font-weight: 800;
    font-size: 18px;
    display: flex;
    align-items: center;
    gap: 6px;
  }
  .contact-bar {
    position: absolute;
    left: 0;
    top: 320px;
    width: 1160px;
    height: 68px;
    display: flex;
    align-items: center;
    padding-left: 38px;
    color: var(--white);
    font-weight: 800;
    font-size: 46px;
    box-sizing: border-box;
  }
  .contact-divider {
    display: inline-block;
    width: 2px;
    height: 40px;
    background: var(--white);
    margin: 0 16px;
  }
</style>
</head>
<body>
  <div class="billboard">
    <svg class="billboard-shapes" width="1160" height="388" viewBox="0 0 1160 388" aria-hidden="true">
      <polygon points="0,0 350,0 271,320 0,320" fill="var(--teal)"/>
      <polygon points="357,0 374,0 295,320 278,320" fill="var(--silver)"/>
      <rect x="0" y="320" width="1160" height="68" fill="var(--ink)"/>
      <polygon points="952,285 1160,285 1160,320 943,320" fill="var(--alert)"/>
    </svg>

    <div class="doctor-photo" role="img" aria-label="Portrait photo of Dr. Lorvik Tamsen in a dark suit and red tie"></div>
    <div class="doctor-name">LORVIK<br>TAMSEN</div>

    <div class="practice-name">KESTREL<br>ORAL<br>SURGERY</div>

    <ul class="services">
      <li class="service"><svg viewBox="0 0 50 50"><circle cx="25" cy="25" r="25" fill="var(--teal)"/><path d="M14 26 L22 34 L37 17" stroke="#fff" stroke-width="6" fill="none" stroke-linecap="round" stroke-linejoin="round"/></svg>IMPLANTS</li>
      <li class="service"><svg viewBox="0 0 50 50"><circle cx="25" cy="25" r="25" fill="var(--teal)"/><path d="M14 26 L22 34 L37 17" stroke="#fff" stroke-width="6" fill="none" stroke-linecap="round" stroke-linejoin="round"/></svg>WISDOM TEETH</li>
      <li class="service"><svg viewBox="0 0 50 50"><circle cx="25" cy="25" r="25" fill="var(--teal)"/><path d="M14 26 L22 34 L37 17" stroke="#fff" stroke-width="6" fill="none" stroke-linecap="round" stroke-linejoin="round"/></svg>JAW SURGERY</li>
      <li class="service"><svg viewBox="0 0 50 50"><circle cx="25" cy="25" r="25" fill="var(--teal)"/><path d="M14 26 L22 34 L37 17" stroke="#fff" stroke-width="6" fill="none" stroke-linecap="round" stroke-linejoin="round"/></svg>FACIAL TRAUMA</li>
    </ul>

    <div class="location-tab">
      <svg width="16" height="24" viewBox="0 0 16 24" aria-hidden="true"><path d="M8 1 C3.6 1 1 4.2 1 8 C1 13 8 23 8 23 C8 23 15 13 15 8 C15 4.2 12.4 1 8 1 Z" fill="#fff"/><circle cx="8" cy="8" r="3" fill="var(--alert)"/></svg>
      WE ARE IN ADA
    </div>

    <div class="contact-bar">
      <span class="contact-phone">(580) 555-0142</span>
      <span class="contact-divider"></span>
      <span class="contact-web">www.kestreloral.com</span>
    </div>
  </div>
</body>
</html>
```